Wirelumo

I'm looking to much improve our current website wirelumo.com
Updates

Low design quality

Target Market(s)

Commercial clients (Not-Residentials)

Industry/Entity Type

Office buildings and Industrial clients

Coding

Coded - Design and coding required

Number of Pages Required

5+ page

Requirements
Must have
• Very professional structured low voltage cabling projects for Wi-Fi, Audio/Video conference rooms, Access Control systems, CCTV.

```html
<!DOCTYPE html>
<html lang="en">
<head>
<meta charset="utf-8">
<title>Wirelumo – Structured Cabling &amp; Low Voltage Engineering</title>
<link href="https://fonts.googleapis.com/css2?family=Oswald:wght@500;600&family=Poppins:wght@400;500;600&display=swap" rel="stylesheet">
<style>
:root{
  --red:#d62b26;
  --red-dark:#b81f1b;
  --ink:#141414;
  --text:#3a3a3a;
  --muted:#6b6b6b;
  --gray-bg:#efefef;
  --pink:#fde0de;
  --line:#e2e2e2;
  --footer:#0f0f10;
  --white:#ffffff;
}
*{box-sizing:border-box;margin:0;padding:0}
html,body{width:1200px;height:5314px;overflow:hidden;background:var(--white)}
body{font-family:"Poppins",sans-serif;color:var(--text);position:relative}
.abs{position:absolute}
.head{font-family:"Oswald",sans-serif;font-weight:600;text-transform:uppercase;color:var(--ink);line-height:1.1}
.head .accent{color:var(--red)}
.eyebrow{font-family:"Oswald",sans-serif;font-weight:500;color:var(--red);text-transform:uppercase;font-size:15px;letter-spacing:.3px}
.btn{position:absolute;display:flex;align-items:center;justify-content:space-between;background:var(--red);color:var(--white);font-size:13px;font-weight:500;text-transform:uppercase;border-radius:6px;padding:0 8px 0 14px}
.btn .arrow{width:28px;height:28px;border-radius:5px;background:var(--white);display:flex;align-items:center;justify-content:center}
.center{left:0;width:1200px;text-align:center}
.rule{position:absolute;left:565px;width:70px;height:4px;background:var(--red);border-radius:2px}

/* top bar + nav */
.topbar{top:0;left:0;width:1200px;height:37px;background:var(--red);color:var(--white);font-size:12.5px}
.topbar .social{position:absolute;left:140px;top:11px;display:flex;gap:10px}
.topbar .social span{width:13px;height:13px;border-radius:50%;background:var(--white)}
.topbar .contact{position:absolute;right:140px;top:10px;display:flex;gap:26px}
.nav{top:37px;left:0;width:1200px;height:83px;background:var(--white)}
.brand{position:absolute;display:flex;align-items:center;gap:8px;font-family:"Oswald",sans-serif;font-weight:600}
.brand .mark{background:var(--red)}
.nav .brand{left:140px;top:18px;font-size:40px;color:var(--ink)}
.nav .brand .mark{width:36px;height:36px}
.nav .menu{position:absolute;left:583px;top:34px;display:flex;gap:22px;font-size:12.5px;font-weight:500;color:var(--ink)}
.nav .btn{left:888px;top:20px;width:172px;height:42px}

/* hero */
.hero{top:120px;left:0;width:1200px;height:530px;border-radius:0 0 90px 90px;overflow:hidden;background:linear-gradient(100deg,#ffffff 0%,#eef4f9 38%,#b9d0e3 70%,#8fb1cd 100%)}
.hero .photo{position:absolute;left:560px;top:0;width:640px;height:530px;background:radial-gradient(circle at 60% 45%,#f2f4f6 0 18%,transparent 40%),linear-gradient(160deg,#c8dbe9,#7da0bf)}
.hero .fade{position:absolute;left:420px;top:0;width:300px;height:530px;background:linear-gradient(90deg,#f4f8fb,rgba(244,248,251,0))}
.hero .tag{left:140px;top:118px;background:#fbe3e1;color:var(--red);font-size:11px;padding:6px 12px;border-radius:14px;text-transform:uppercase}
.hero h1{left:140px;top:156px;font-size:43px}
.hero h1 .thin{font-weight:500}
.hero p{left:140px;top:253px;width:420px;font-size:13px;line-height:1.65;color:var(--text)}
.hero .btn{left:140px;top:338px;width:237px;height:42px}

/* about */
.about-img1{left:140px;top:734px;width:332px;height:316px;border-radius:18px;background:linear-gradient(135deg,#6d6a63,#c9b59a 45%,#3e4a58)}
.about-img2{left:291px;top:951px;width:270px;height:276px;border-radius:18px;border:6px solid var(--white);background:linear-gradient(135deg,#e8e4de,#d79a5c 50%,#8a6b4a)}
.badge{left:227px;top:965px;width:124px;height:124px;border-radius:50%;background:var(--white);box-shadow:0 6px 20px rgba(0,0,0,.12)}
.badge .core{position:absolute;left:37px;top:37px;width:50px;height:50px;border-radius:50%;background:var(--red)}
.about .eyebrow{left:610px;top:732px}
.about h2{left:610px;top:754px;font-size:40px}
.about .lead{left:610px;top:868px;width:420px;font-size:11.5px;font-weight:600;color:var(--ink);text-transform:uppercase;line-height:1.8}
.about .body{left:610px;top:908px;width:420px;font-size:12.5px;line-height:1.7}
.about .btn{left:610px;top:1031px;width:136px;height:40px}
.stats{left:610px;top:1099px;width:448px;height:132px;background:var(--white);border-radius:12px;box-shadow:0 6px 24px rgba(0,0,0,.1)}
.stats .thumb{position:absolute;left:14px;top:14px;width:130px;height:104px;border-radius:8px;background:linear-gradient(135deg,#4a6a8a,#c9d4de 50%,#6f7f8c)}
.stat{position:absolute;top:34px}
.stat b{display:block;font-family:"Oswald",sans-serif;font-weight:600;color:var(--red);font-size:34px;line-height:1}
.stat span{font-size:12px;color:var(--text)}

/* services */
.services{top:1320px;left:0;width:1200px;height:1118px;background:var(--gray-bg);border-radius:60px}
.services .eyebrow{top:80px}
.services h2{top:96px;font-size:40px}
.services .rule{top:196px}
.card{position:absolute;width:290px;height:390px;background:var(--white);border-radius:14px;overflow:hidden;text-align:center}
.card .pic{height:206px}
.card .icon{position:absolute;left:108px;top:168px;width:74px;height:74px;border-radius:50%;background:var(--red);border:5px solid var(--white);display:flex;align-items:center;justify-content:center}
.card h3{font-family:"Oswald",sans-serif;font-weight:600;font-size:21px;color:var(--ink);text-transform:uppercase;margin-top:52px}
.card p{font-size:12px;line-height:1.7;color:var(--muted);padding:6px 24px 0}
.card.no-title p{margin-top:84px}

/* features */
.features .eyebrow{top:2523px}
.features h2{top:2541px;font-size:40px}
.features .intro{top:2662px;font-size:12.5px;line-height:1.65;color:var(--muted)}
.hub{left:505px;top:2832px;width:186px;height:186px;border-radius:50%;background:var(--white);box-shadow:0 10px 36px rgba(0,0,0,.12);display:flex;align-items:center;justify-content:center}
.hub .brand{position:static;font-size:28px;color:var(--ink);gap:6px}
.hub .brand .mark{width:22px;height:22px}
.pill{position:absolute;width:235px;height:83px;border:2px solid var(--line);border-radius:42px;background:var(--white);display:flex;align-items:center;font-size:15px;font-weight:600;color:var(--ink);line-height:1.25}
.pill.left{justify-content:flex-end;text-align:right;padding-right:8px}
.pill.right{padding-left:8px}
.pill .dot{width:66px;height:66px;border-radius:50%;display:flex;align-items:center;justify-content:center;flex:none}
.pill.left .dot{margin-left:12px}
.pill.right .dot{margin-right:12px}
.dot.red{background:var(--red)}
.dot.dark{background:var(--ink)}

/* end to end */
.e2e{top:3210px;left:0;width:1200px;height:643px;background:var(--gray-bg);border-radius:60px}
.e2e .eyebrow{left:140px;top:107px}
.e2e h2{left:140px;top:122px;font-size:42px;line-height:1.06}
.checks{position:absolute;left:140px;top:290px;list-style:none}
.checks li{display:flex;align-items:center;gap:9px;font-size:13px;font-weight:500;color:var(--ink);height:37px}
.checks li i{width:16px;height:16px;border-radius:50%;background:var(--red);display:flex;align-items:center;justify-content:center}
.e2e .btn{left:140px;top:518px;width:237px;height:42px}
.e2e .pic1{left:540px;top:85px;width:161px;height:476px;border-radius:16px;background:linear-gradient(160deg,#4a9bd0,#e9572d 45%,#d84a3c 60%,#2d5f8a)}
.e2e .pic2{left:722px;top:85px;width:336px;height:476px;border-radius:16px;background:linear-gradient(135deg,#d9d6cf,#a9a49b 50%,#efece6)}

/* cta */
.cta{left:140px;top:3944px;width:918px;height:395px;border-radius:40px;background:var(--pink);overflow:hidden}
.cta .pic{position:absolute;left:0;top:0;width:520px;height:395px;background:linear-gradient(135deg,#132a6b,#2a57b8 45%,#d9c53a 60%,#0f1c3f);clip-path:polygon(0 0,100% 0,82% 100%,0 100%)}
.cta .eyebrow{left:528px;top:78px;font-size:14px}
.cta h2{left:528px;top:92px;font-size:37px;line-height:1.1}
.cta p{left:528px;top:234px;width:260px;font-size:12.5px;line-height:1.55;color:var(--ink)}
.cta .btn{left:528px;top:295px;width:167px;height:42px}

/* contact */
.contact .eyebrow{top:4423px}
.contact h2{top:4440px;font-size:40px}
.contact .rule{top:4501px}
.field{position:absolute;border:1.5px solid var(--line);border-radius:4px;font-size:12px;color:#9a9a9a;display:flex;align-items:center;padding-left:14px;gap:14px;background:var(--white)}
.field i{width:14px;height:14px;border:1.5px solid #bdbdbd;border-radius:3px}
.field.msg{align-items:flex-start;padding-top:16px}
.submit{left:293px;top:4809px;width:615px;height:49px;background:var(--red);border-radius:4px;color:var(--white);font-size:12px;font-weight:600;text-transform:uppercase;display:flex;align-items:center;justify-content:center}

/* footer */
.footer{top:4945px;left:0;width:1200px;height:369px;background:var(--footer);border-radius:80px 80px 0 0;color:#cfcfcf;font-size:12.5px}
.footer .brand{left:140px;top:80px;font-size:40px;color:var(--white)}
.footer .brand .mark{width:34px;height:34px}
.footer .about-text{position:absolute;left:140px;top:150px;width:270px;line-height:1.65;font-size:12px}
.footer h4{position:absolute;top:78px;font-family:"Oswald",sans-serif;font-weight:500;color:var(--white);font-size:17px;text-transform:uppercase}
.footer .col{position:absolute;top:112px;line-height:1.6}
.footer .links p{margin-bottom:9px}
.footer .info p{display:flex;gap:8px;margin-bottom:16px}
.footer .info i{width:10px;height:10px;border-radius:50%;background:var(--white);margin-top:5px;flex:none}
.footer .social-list p{display:flex;align-items:center;gap:10px;margin-bottom:12px}
.footer .social-list span{width:30px;height:30px;border-radius:50%;background:var(--red)}
.footer .social-list p:nth-child(n+2) span{background:#2b2b2e}
.footer .divider{position:absolute;left:140px;top:305px;width:918px;height:1px;background:#2d2d30}
.footer .copy{position:absolute;left:0;width:1200px;top:330px;text-align:center;font-size:12px}
</style>
</head>
<body>

<!-- top bar -->
<div class="abs topbar">
  <div class="social"><span></span><span></span><span></span><span></span></div>
  <div class="contact"><span>&#9993; Email: info@northlineworks.com</span><span>&#9742; Phone: 301-555-0190</span></div>
</div>

<!-- navigation -->
<header class="abs nav">
  <div class="brand"><span class="mark"></span>Wirelumo</div>
  <nav class="menu"><span>HOME</span><span>ABOUT US</span><span>SERVICES</span><span>CONTACT</span></nav>
  <div class="btn">Request Quote <span class="arrow"><svg width="16" height="12" viewBox="0 0 16 12"><path d="M1 6h13M9 1l5 5-5 5" stroke="#141414" stroke-width="2" fill="none"/></svg></span></div>
</header>

<!-- hero -->
<section class="abs hero">
  <div class="photo" role="img" aria-label="Dome security camera mounted on a pole against a modern glass building"></div>
  <div class="fade"></div>
  <div class="abs tag">Commercial only · B2B Enterprise</div>
  <h1 class="abs head">Structured Cabling<br><span class="thin">&amp; Low Voltage Engineering</span></h1>
  <p class="abs">High-Performance Copper, Fiber Optic, And Wireless Network Architecture Built Exclusively For Modern Corporate Offices, Industrial Complexes, And Commercial Facilities.</p>
  <div class="btn">Consult Our Engineers <span class="arrow"><svg width="16" height="12" viewBox="0 0 16 12"><path d="M1 6h13M9 1l5 5-5 5" stroke="#141414" stroke-width="2" fill="none"/></svg></span></div>
</section>

<!-- about -->
<section class="about">
  <div class="abs about-img1" role="img" aria-label="Technician in hard hat and safety glasses working on a network panel"></div>
  <div class="abs about-img2" role="img" aria-label="Electrical connectors, cable ties and wiring tools on a table"></div>
  <div class="abs badge">
    <svg class="abs" width="124" height="124" viewBox="0 0 124 124"><defs><path id="ring" d="M62 62m-46 0a46 46 0 1 1 92 0a46 46 0 1 1-92 0"/></defs><text font-family="Poppins,sans-serif" font-size="10" font-weight="600" fill="#141414" letter-spacing="1"><textPath href="#ring">Years Of 25+ Years Of Experience · Experience ·</textPath></text></svg>
    <div class="core"></div>
  </div>
  <div class="abs eyebrow">About Us</div>
  <h2 class="abs head">Wirelumo: Your Trusted<br><span class="accent">Cabling Partner</span></h2>
  <p class="abs lead">Elevate Your Connectivity With Wirelumo's Low Voltage Cabling Solutions.</p>
  <p class="abs body">Wirelumo Is Your Premier Provider Of Professional Low Voltage Cabling Services In Virginia, Washington DC, And Maryland. With A Focus On Quality, Reliability, And Attention To Detail, We Deliver Exceptional Cabling Solutions For Audio, Video, Security Systems, Computer Networks, And More.</p>
  <div class="btn">Read More <span class="arrow"><svg width="16" height="12" viewBox="0 0 16 12"><path d="M1 6h13M9 1l5 5-5 5" stroke="#141414" stroke-width="2" fill="none"/></svg></span></div>
  <div class="abs stats">
    <div class="thumb" role="img" aria-label="Server rack with patch panels"></div>
    <div class="stat" style="left:166px"><b>1k+</b><span>Projects Completed</span></div>
    <div class="stat" style="left:308px"><b>100%</b><span>Commercial Focus</span></div>
  </div>
</section>

<!-- services -->
<section class="abs services">
  <div class="abs eyebrow center">What We Do</div>
  <h2 class="abs head center">Infrastructure Solutions That<br><span class="accent">Keep Business Moving.</span></h2>
  <div class="rule"></div>

  <article class="card" style="left:140px;top:229px">
    <div class="pic" role="img" aria-label="Hands organising blue network cables in a rack" style="background:linear-gradient(135deg,#d9dee3,#3f78b8 55%,#1c3f6e)"></div>
    <div class="icon"><svg width="30" height="30" viewBox="0 0 30 30"><rect x="7" y="5" width="5" height="20" rx="2" fill="#fff"/><rect x="18" y="5" width="5" height="20" rx="2" fill="#fff"/></svg></div>
    <h3>Structured Cabling</h3>
    <p>Cat6A / Cat7 Copper &amp; Single-Mode/ Multimode Fiber Backbone For High-Speed Data, PoE, And Future 10G/40G Readiness.</p>
  </article>
  <article class="card" style="left:456px;top:229px">
    <div class="pic" role="img" aria-label="Installer on a ladder mounting an outdoor camera among trees" style="background:linear-gradient(135deg,#3f5f2b,#8ab04a 50%,#2f4a24)"></div>
    <div class="icon"><svg width="30" height="30" viewBox="0 0 30 30"><rect x="4" y="8" width="18" height="10" rx="2" fill="#fff"/><rect x="12" y="18" width="3" height="8" fill="#fff"/><rect x="8" y="24" width="12" height="3" fill="#fff"/></svg></div>
    <h3>Video Surveillance (CCTV)</h3>
    <p>4K IP Cameras, NVRs, AI-Powered Analytics, And Remote Monitoring For Full-Site Security And Compliance.</p>
  </article>
  <article class="card" style="left:769px;top:229px">
    <div class="pic" role="img" aria-label="Hand holding a phone to a door access reader" style="background:linear-gradient(135deg,#9aa3ab,#4d5660 50%,#c9cdd1)"></div>
    <div class="icon"><svg width="30" height="30" viewBox="0 0 30 30"><rect x="8" y="4" width="14" height="22" rx="3" fill="none" stroke="#fff" stroke-width="2.5"/><circle cx="15" cy="15" r="3" fill="#fff"/></svg></div>
    <h3>Access Control Systems</h3>
    <p>Biometric, RFID, Mobile Credentials, And Cloud-Managed Door Access With Audit Trails And Emergency Integration.</p>
  </article>
  <article class="card" style="left:140px;top:643px">
    <div class="pic" role="img" aria-label="Open-plan office with desks and large windows" style="background:linear-gradient(135deg,#5a5a5a,#cfcfcf 50%,#3b3b3b)"></div>
    <div class="icon"><svg width="30" height="30" viewBox="0 0 30 30"><rect x="4" y="14" width="22" height="9" rx="2" fill="#fff"/><path d="M9 14V7M15 14V5M21 14V7" stroke="#fff" stroke-width="2.5"/></svg></div>
    <h3>Wireless Access Points</h3>
    <p>Enterprise-Grade Wi-Fi 6/6E, Site Surveys, Seamless Roaming, And High-Density Deployments For Offices &amp; Warehouses.</p>
  </article>
  <article class="card no-title" style="left:456px;top:643px">
    <div class="pic" role="img" aria-label="Conference room with long table and wall display" style="background:linear-gradient(135deg,#6b4a2f,#e8e3dc 50%,#3a2a1e)"></div>
    <div class="icon"><svg width="30" height="30" viewBox="0 0 30 30"><circle cx="15" cy="9" r="4" fill="#fff"/><circle cx="7" cy="12" r="3" fill="#fff"/><circle cx="23" cy="12" r="3" fill="#fff"/><rect x="4" y="18" width="22" height="6" rx="2" fill="#fff"/></svg></div>
    <p>Video Conferencing (Cloud Meetings), HDMI Distribution, DSP Audio, Auto-Framing Cameras &amp; Interactive Displays.</p>
  </article>
  <article class="card" style="left:769px;top:643px">
    <div class="pic" role="img" aria-label="Customer paying with a phone at a café counter" style="background:linear-gradient(135deg,#3a2a20,#b08566 50%,#1f1915)"></div>
    <div class="icon"><svg width="30" height="30" viewBox="0 0 30 30"><rect x="6" y="4" width="18" height="9" rx="2" fill="#fff"/><rect x="6" y="15" width="18" height="11" rx="2" fill="#fff"/></svg></div>
    <h3>Point Of Sale (POS)</h3>
    <p>Resilient Cabling For Retail POS, Payment Terminals, And Inventory Systems With EMI Shielding And High Availability.</p>
  </article>
</section>

<!-- features -->
<section class="features">
  <div class="abs eyebrow center">Why Choose Us</div>
  <h2 class="abs head center">Key Features Of Wirelumo's<br><span class="accent">Cabling Services</span></h2>
  <p class="abs intro center">We Are A Full Service Cabling Company And Will Work With Your IT Staff To Make Sure Everything<br>Up And Running After Installation And Testing.</p>

  <svg class="abs" style="left:0;top:2700px" width="1200" height="440" viewBox="0 0 1200 440">
    <g stroke="#d8d8d8" stroke-width="2" fill="none">
      <path d="M437 64H470Q480 64 480 74V150Q480 160 490 160H505"/>
      <path d="M375 170H460Q470 170 470 180V205"/>
      <path d="M375 275H460Q470 275 470 265V240"/>
      <path d="M437 382H470Q480 382 480 372V290Q480 280 490 280H505"/>
      <path d="M759 64H726Q716 64 716 74V150Q716 160 706 160H691"/>
      <path d="M825 170H740Q730 170 730 180V205"/>
      <path d="M825 275H740Q730 275 730 265V240"/>
      <path d="M759 382H726Q716 382 716 372V290Q716 280 706 280H691"/>
    </g>
    <g fill="#d62b26">
      <circle cx="437" cy="64" r="4"/><circle cx="375" cy="170" r="4"/><circle cx="375" cy="275" r="4"/><circle cx="437" cy="382" r="4"/>
      <circle cx="759" cy="64" r="4"/><circle cx="825" cy="170" r="4"/><circle cx="825" cy="275" r="4"/><circle cx="759" cy="382" r="4"/>
    </g>
  </svg>

  <div class="abs hub"><div class="brand"><span class="mark"></span>Wirelumo</div></div>

  <div class="pill left" style="left:202px;top:2723px">Expertise<br>and Experience<span class="dot red"><svg width="28" height="28" viewBox="0 0 28 28"><circle cx="14" cy="9" r="5" fill="#fff"/><path d="M5 25c0-6 4-9 9-9s9 3 9 9z" fill="#fff"/></svg></span></div>
  <div class="pill left" style="left:140px;top:2828px">Comprehensive<br>Solution<span class="dot dark"><svg width="28" height="28" viewBox="0 0 28 28"><circle cx="14" cy="14" r="9" fill="none" stroke="#fff" stroke-width="2.5"/><path d="M14 8v6l4 3" stroke="#fff" stroke-width="2.5" fill="none"/></svg></span></div>
  <div class="pill left" style="left:140px;top:2933px">Quality<br>Workmanship<span class="dot red"><svg width="28" height="28" viewBox="0 0 28 28"><circle cx="14" cy="12" r="8" fill="none" stroke="#fff" stroke-width="2.5"/><path d="M9 19l-2 7 7-3 7 3-2-7" fill="#fff"/></svg></span></div>
  <div class="pill left" style="left:202px;top:3040px">Commercial<br>and Industrial<span class="dot dark"><svg width="28" height="28" viewBox="0 0 28 28"><rect x="6" y="5" width="16" height="20" fill="none" stroke="#fff" stroke-width="2.5"/><path d="M10 10h2M16 10h2M10 15h2M16 15h2M12 25v-5h4v5" stroke="#fff" stroke-width="2"/></svg></span></div>

  <div class="pill right" style="left:759px;top:2723px"><span class="dot red"><svg width="28" height="28" viewBox="0 0 28 28"><path d="M8 4v12M4 12l4 4 4-4M20 4v12M16 12l4 4 4-4" stroke="#fff" stroke-width="2.5" fill="none"/><circle cx="14" cy="22" r="4" fill="#fff"/></svg></span>Low Cost</div>
  <div class="pill right" style="left:825px;top:2828px"><span class="dot dark"><svg width="28" height="28" viewBox="0 0 28 28"><circle cx="14" cy="10" r="5" fill="#fff"/><path d="M5 25c0-6 4-9 9-9s9 3 9 9z" fill="#fff"/></svg></span>Customer<br>Satisfaction</div>
  <div class="pill right" style="left:825px;top:2933px"><span class="dot red"><svg width="28" height="28" viewBox="0 0 28 28"><path d="M14 3l9 4v7c0 6-4 10-9 12-5-2-9-6-9-12V7z" fill="#fff"/></svg></span>Safe &amp; Secure</div>
  <div class="pill right" style="left:759px;top:3040px"><span class="dot dark"><svg width="28" height="28" viewBox="0 0 28 28"><rect x="3" y="5" width="22" height="10" rx="2" fill="none" stroke="#fff" stroke-width="2.2"/><circle cx="8" cy="20" r="3" fill="#fff"/><circle cx="14" cy="20" r="3" fill="#fff"/><circle cx="20" cy="20" r="3" fill="#fff"/></svg></span>Customer<br>Satisfaction</div>
</section>

<!-- end to end -->
<section class="abs e2e">
  <div class="abs eyebrow">Wirelumo</div>
  <h2 class="abs head">End-to-End Physical<br>Network <span class="accent">And</span><br><span class="accent">Cabling Services</span></h2>
  <ul class="checks">
    <li><i><svg width="9" height="8" viewBox="0 0 9 8"><path d="M1 4l2.5 2.5L8 1" stroke="#fff" stroke-width="1.8" fill="none"/></svg></i>Voice &amp; Data Cable Installations</li>
    <li><i><svg width="9" height="8" viewBox="0 0 9 8"><path d="M1 4l2.5 2.5L8 1" stroke="#fff" stroke-width="1.8" fill="none"/></svg></i>Copper Cable CAT6 And CAT7</li>
    <li><i><svg width="9" height="8" viewBox="0 0 9 8"><path d="M1 4l2.5 2.5L8 1" stroke="#fff" stroke-width="1.8" fill="none"/></svg></i>3Fiber Cable Single &amp; Multi Mode</li>
    <li><i><svg width="9" height="8" viewBox="0 0 9 8"><path d="M1 4l2.5 2.5L8 1" stroke="#fff" stroke-width="1.8" fill="none"/></svg></i>Conduit Installations</li>
    <li><i><svg width="9" height="8" viewBox="0 0 9 8"><path d="M1 4l2.5 2.5L8 1" stroke="#fff" stroke-width="1.8" fill="none"/></svg></i>IDF And MDF Installations</li>
    <li><i><svg width="9" height="8" viewBox="0 0 9 8"><path d="M1 4l2.5 2.5L8 1" stroke="#fff" stroke-width="1.8" fill="none"/></svg></i>Certified LX-8000 Certification</li>
  </ul>
  <div class="btn">Consult Our Engineers <span class="arrow"><svg width="16" height="12" viewBox="0 0 16 12"><path d="M1 6h13M9 1l5 5-5 5" stroke="#141414" stroke-width="2" fill="none"/></svg></span></div>
  <div class="abs pic1" role="img" aria-label="Hand plugging a red patch cable into a switch with blue lights"></div>
  <div class="abs pic2" role="img" aria-label="Wall-mounted bullet security cameras on a stone facade"></div>
</section>

<!-- cta -->
<section class="abs cta">
  <div class="pic" role="img" aria-label="Close-up of blue and yellow network patch cables in a switch"></div>
  <div class="abs eyebrow">Start The Conversation</div>
  <h2 class="abs head">Planning A Commercial<br>Cabling <span class="accent">Or Technology</span><br><span class="accent">Project?</span></h2>
  <p class="abs">Planning A Commercial Cabling Or Technology Project?</p>
  <div class="btn">Call Us Today <span class="arrow"><svg width="16" height="12" viewBox="0 0 16 12"><path d="M1 6h13M9 1l5 5-5 5" stroke="#141414" stroke-width="2" fill="none"/></svg></span></div>
</section>

<!-- contact -->
<section class="contact">
  <div class="abs eyebrow center">Contact Us</div>
  <h2 class="abs head center">Request A <span class="accent">Quote Today</span></h2>
  <div class="rule"></div>
  <div class="field" style="left:293px;top:4543px;width:299px;height:49px"><i></i>First Name</div>
  <div class="field" style="left:609px;top:4543px;width:299px;height:49px"><i></i>Last Name</div>
  <div class="field" style="left:293px;top:4611px;width:299px;height:49px"><i></i>Your Email</div>
  <div class="field" style="left:609px;top:4611px;width:299px;height:49px"><i></i>Phone</div>
  <div class="field msg" style="left:293px;top:4679px;width:615px;height:103px"><i></i>Your Message</div>
  <div class="abs submit">Submit Now</div>
</section>

<!-- footer -->
<footer class="abs footer">
  <div class="brand"><span class="mark"></span>Wirelumo</div>
  <p class="about-text">Wirelumo Is A Local Group Of IT Professionals, Dedicated To Fast, Reliable And Honest Service. No Job Is Too Big Or Too Small, Get In Touch Today For Solutions To All Your IT Infrastructure Needs!</p>

  <h4 style="left:489px">Quick Links</h4>
  <div class="col links" style="left:491px;top:108px"><p>Home</p><p>About Us</p><p>Services</p><p>Contact</p></div>

  <h4 style="left:664px">Contact Details</h4>
  <div class="col info" style="left:664px">
    <p><i></i><span>Local: 703-555-0148<br>National: (888) 555-0125</span></p>
    <p><i></i><span>Phone<br>+123 555 0124</span></p>
    <p><i></i><span>Email<br>sales@wirelumo.com</span></p>
  </div>

  <h4 style="left:939px">Social Media</h4>
  <div class="col social-list" style="left:939px;top:108px">
    <p><span></span>Community</p>
    <p><span></span>Video Channel</p>
    <p><span></span>Professional Network</p>
    <p><span></span>Photo Gallery</p>
  </div>

  <div class="divider"></div>
  <p class="copy">© 2026 Wirelumo. All Rights Reserved.</p>
</footer>

</body>
</html>
```